Logo & Visitenkarte für Mentoring  und Supervision
Logo & Visitenkarte für Mentoring und Supervision
Zielgruppe
Ich gehe für eine neue verkörperte weibliche Spiritualität.
Ich biete Mentoring und Supervision für Mädchen und Frauen an.
Ich halte Raum für Mädchen und Frauenkreise, Retreate und Fortbildungen.
Ich halte die Vision von einem Yogini-Dorf und bin dabei eine Stiftung zu gründen.
Meine Zielgruppe: Mädchen und Frauen, die verbunden mit Himmel und Erde selbstermächtigt ihr Leben leben und ihre ganz spezielle Gabe in die Welt bringen: ganz schön stark
Aufgabenstellung
Ganzheit. Schönheit. Stärke
sollen in diesem sehr weiblichen Raum für Mädchen und Frauen ausgestrahlt werden.
Frauenzeichen und Raum verbinden

```html
<!DOCTYPE html>
<html lang="de">
<head>
<meta charset="utf-8">
<title>Marlene Vogt – Visitenkarte</title>
<link rel="stylesheet" href="https://fonts.googleapis.com/css2?family=Montserrat:wght@500;600&display=swap">
<style>
  :root {
    --page: #ffffff;
    --maroon: #5c062b;
    --gold: #ecc064;
    --gold-light: #f2d488;
    --gold-deep: #d68a14;
    --red: #c01d2a;
  }
  html, body {
    margin: 0;
    padding: 0;
    width: 1200px;
    height: 1199px;
    overflow: hidden;
    background: var(--page);
  }
  .card {
    position: absolute;
    left: 311px;
    width: 585px;
    height: 379px;
    background: var(--maroon);
    overflow: hidden;
    font-family: "Montserrat", sans-serif;
    text-align: center;
    color: var(--gold);
  }
  .card--front { top: 137px; }
  .card--back  { top: 672px; }

  .brand-dot {
    position: absolute;
    left: 192px;
    top: 57px;
    width: 200px;
    height: 200px;
    border-radius: 50%;
    background: var(--gold-deep);
  }
  .brand-name {
    position: absolute;
    left: 0;
    right: 0;
    margin: 0;
    font-weight: 600;
    color: var(--gold);
    letter-spacing: 0.5px;
  }
  .card--front .brand-name { top: 258px; font-size: 38px; }
  .card--back .brand-name  { top: 28px;  font-size: 36px; }

  .tagline {
    position: absolute;
    left: 0;
    right: 0;
    top: 320px;
    margin: 0;
    font-size: 15px;
    font-weight: 600;
  }
  .sep { color: var(--red); padding: 0 2px; }

  .service {
    position: absolute;
    left: 0;
    right: 0;
    top: 89px;
    margin: 0;
    font-size: 15.5px;
    font-weight: 600;
    color: var(--red);
  }
  .contact {
    position: absolute;
    left: 0;
    right: 0;
    top: 138px;
    margin: 0;
    font-style: normal;
    font-size: 15.5px;
    font-weight: 500;
    line-height: 23px;
    letter-spacing: 0.6px;
  }
  .contact .address { display: block; margin-bottom: 5px; }
  .contact span { display: block; }

  .gold-band {
    position: absolute;
    left: 0;
    top: 0;
    width: 585px;
    height: 379px;
  }
</style>
</head>
<body>
  <section class="card card--front">
    <div class="brand-dot" aria-hidden="true"></div>
    <h1 class="brand-name">Marlene Vogt</h1>
    <p class="tagline">Raum für Ganzheit <span class="sep">•</span> Schönheit <span class="sep">•</span> Stärke</p>
  </section>

  <section class="card card--back">
    <svg class="gold-band" viewBox="0 0 585 379" aria-hidden="true">
      <defs>
        <linearGradient id="bandGold" x1="0" y1="0" x2="0" y2="1">
          <stop offset="0" stop-color="#f2d488"/>
          <stop offset="1" stop-color="#d68a14"/>
        </linearGradient>
      </defs>
      <path d="M0 215 Q292.5 470 585 215 L585 379 L0 379 Z" fill="url(#bandGold)"/>
    </svg>
    <h2 class="brand-name">Marlene Vogt</h2>
    <p class="service">Mentoring &amp; Supervision für Mädchen und Frauen</p>
    <address class="contact">
      <span class="address">Lindenweg 7 <span class="sep" style="display:inline">•</span> 54321 Beispielstadt</span>
      <span>0171 52 60 418</span>
      <span>info@marlene-vogt.de</span>
      <span>www.marlene-vogt.de</span>
    </address>
  </section>
</body>
</html>
```